Ward Compass Business Card Design*

We need a business card design for our company Ward Compass. Our company is specialized in providing online consulting services regarding medical institutions, hospitals and doctors. We work with patients worldwide looking to choose between healthcare providers. We have a website you may use as a reference, where we list doctors and clinics worldwide. So we target Medical providers as well as patients worldwide.
Target Market(s)
Medical Providers and patients around the world
Industry/Entity Type
Medical
Contact Information for Business Card
Salma Driouch
CEO
+90 612 348 2751
info@wardcompass.example
www.wardcompass.example
17 Essafsaf 3 H.Q.L. Rabat, Morocco
Requirements
Must have
- Company logo/name on one full side, personal info and smaller logo and company name on the other side.
Nice to have
- Smart and elegant design

```html
<!DOCTYPE html>
<html lang="en">
<head>
<meta charset="UTF-8">
<title>Ward Compass Business Card</title>
<link href="https://fonts.googleapis.com/css2?family=Poppins:wght@400;600&display=swap" rel="stylesheet">
<style>
  :root {
    --navy: #143a6b;
    --navy-deep: #10345f;
    --white: #ffffff;
    --ring: #8c8c8c;
    --backdrop: #e4e6ea;
  }
  html, body {
    margin: 0;
    padding: 0;
    width: 1200px;
    height: 960px;
    overflow: hidden;
    background: var(--backdrop);
    font-family: "Poppins", sans-serif;
  }
  .stage {
    position: relative;
    width: 1200px;
    height: 960px;
  }
  .card {
    position: absolute;
    left: 250px;
    width: 700px;
    height: 400px;
    overflow: hidden;
    box-shadow: 0 10px 28px rgba(0,0,0,0.18);
  }
  .card-front {
    top: 50px;
    background: var(--navy);
    display: flex;
    align-items: center;
    justify-content: center;
  }
  .card-back {
    top: 510px;
    background: var(--navy-deep);
  }
  .brand {
    display: flex;
    align-items: center;
    gap: 14px;
    font-weight: 600;
    letter-spacing: 1px;
    text-transform: uppercase;
  }
  .brand-mark {
    border-radius: 50%;
    box-sizing: border-box;
  }
  .card-front .brand { color: var(--white); font-size: 30px; }
  .card-front .brand-mark { width: 46px; height: 46px; border: 6px solid var(--white); }
  .card-back .brand {
    position: absolute;
    left: 370px;
    top: 160px;
    color: var(--navy);
    font-size: 21px;
  }
  .card-back .brand-mark { width: 34px; height: 34px; border: 5px solid var(--navy); }
  .back-shapes {
    position: absolute;
    inset: 0;
  }
  .contact {
    position: absolute;
    left: 52px;
    top: 222px;
    color: var(--white);
  }
  .contact-name { margin: 0; font-size: 25px; font-weight: 600; line-height: 1.1; }
  .contact-role { margin: 0 0 12px; font-size: 13px; }
  .contact-address { margin: 0 0 12px; font-size: 13px; line-height: 1.35; }
  .contact-list { list-style: none; margin: 0; padding: 0; font-size: 13px; line-height: 1.5; }
  .contact-list li { display: flex; align-items: center; gap: 10px; }
  .contact-list svg { width: 12px; height: 12px; fill: var(--white); flex: none; }
</style>
</head>
<body>
<main class="stage">
  <section class="card card-front">
    <div class="brand"><span class="brand-mark"></span>Ward Compass</div>
  </section>

  <section class="card card-back">
    <svg class="back-shapes" viewBox="0 0 700 400" aria-hidden="true">
      <polygon points="420,0 700,0 700,215 560,330 460,300" fill="#ffffff"/>
      <circle cx="505" cy="175" r="168" fill="#ffffff" stroke="#8c8c8c" stroke-width="8"/>
    </svg>
    <div class="brand"><span class="brand-mark"></span>Ward Compass</div>
    <div class="contact">
      <h1 class="contact-name">Salma Driouch</h1>
      <p class="contact-role">CEO</p>
      <p class="contact-address">17 Essafsaf 3<br>H.Q.L. Rabat, Morocco</p>
      <ul class="contact-list">
        <li><svg viewBox="0 0 24 24"><path d="M6.6 10.8a15.1 15.1 0 0 0 6.6 6.6l2.2-2.2a1 1 0 0 1 1-.25 11.4 11.4 0 0 0 3.6.57 1 1 0 0 1 1 1V20a1 1 0 0 1-1 1A17 17 0 0 1 3 4a1 1 0 0 1 1-1h3.5a1 1 0 0 1 1 1c0 1.25.2 2.45.57 3.6a1 1 0 0 1-.25 1z"/></svg>+90 612 348 2751</li>
        <li><svg viewBox="0 0 24 24"><path d="M2 5h20v14H2z M2 5l10 8 10-8" /></svg>info@wardcompass.example</li>
        <li><svg viewBox="0 0 24 24"><circle cx="12" cy="12" r="10"/></svg>www.wardcompass.example</li>
      </ul>
    </div>
  </section>
</main>
</body>
</html>
```